Talvex Industrial Maintenance Business Card

Design a business card with the following information, logo must be included.
Talvex Industrial Maintenance
Dale Virnow Jr.
Pone 413-627-8154
email dale.virnow.jr@brindlemail.net

```html
<!DOCTYPE html>
<html lang="en">
<head>
<meta charset="utf-8">
<title>Talvex Industrial Maintenance – Business Card</title>
<link rel="stylesheet" href="https://fonts.googleapis.com/css2?family=Montserrat:wght@400;500;600;700&display=swap">
<style>
  :root {
    --page-bg: #d9d4cc;
    --card-bg: #262626;
    --disc: #2f2f2f;
    --brand-blue: #1c70bf;
    --tagline-grey: #8a8a8a;
    --text-light: #e6e6e6;
    --card-shadow: rgba(0, 0, 0, 0.45);
  }
  * { box-sizing: border-box; margin: 0; padding: 0; }
  html, body { width: 900px; height: 1200px; overflow: hidden; }
  body {
    background: var(--page-bg);
    font-family: "Montserrat", Arial, sans-serif;
    position: relative;
  }
  .card {
    position: absolute;
    left: 80px;
    width: 742px;
    height: 442px;
    border-radius: 30px;
    background: var(--card-bg);
    overflow: hidden;
    box-shadow: 0 8px 18px var(--card-shadow);
  }
  .card--front { top: 130px; }
  .card--back { top: 637px; }

  .brand-disc {
    position: absolute;
    border-radius: 50%;
    background: var(--disc);
  }
  .card--front .brand-disc { left: -5px; top: 25px; width: 380px; height: 380px; }
  .card--back .brand-disc { left: 430px; top: 20px; width: 380px; height: 380px; }

  .wordmark {
    position: absolute;
    font-weight: 600;
    line-height: 1;
    white-space: nowrap;
  }
  .wordmark__name { display: block; color: var(--brand-blue); letter-spacing: 1px; }
  .wordmark__tagline { display: block; color: var(--tagline-grey); font-weight: 700; letter-spacing: 0; }

  .card--front .wordmark { left: 412px; top: 326px; }
  .card--front .wordmark__name { font-size: 62px; }
  .card--front .wordmark__tagline { font-size: 17.5px; margin-top: 2px; }

  .card--back .wordmark { left: 38px; top: 42px; }
  .card--back .wordmark__name { font-size: 79px; }
  .card--back .wordmark__tagline { font-size: 21.5px; margin-top: 2px; }

  .contact-person { position: absolute; left: 38px; top: 286px; }
  .contact-person__name {
    color: var(--brand-blue);
    font-size: 24px;
    font-weight: 700;
  }
  .contact-person__role {
    color: var(--text-light);
    font-size: 16px;
    font-weight: 400;
    margin-top: 0;
  }
  .contact-person__rule {
    width: 18px;
    height: 2px;
    background: var(--brand-blue);
    margin-top: 14px;
  }
  .contact-list {
    position: absolute;
    left: 38px;
    top: 364px;
    list-style: none;
  }
  .contact-list__item {
    display: flex;
    align-items: center;
    gap: 10px;
    color: var(--text-light);
    font-size: 16px;
    height: 24px;
  }
  .contact-list__icon { width: 18px; height: 18px; flex: none; }
</style>
</head>
<body>

<section class="card card--front" aria-label="Card front">
  <div class="brand-disc"></div>
  <div class="wordmark">
    <span class="wordmark__name">TALVEX</span>
    <span class="wordmark__tagline">INDUSTRIAL MAINTENANCE</span>
  </div>
</section>

<section class="card card--back" aria-label="Card back">
  <div class="brand-disc"></div>
  <div class="wordmark">
    <span class="wordmark__name">TALVEX</span>
    <span class="wordmark__tagline">INDUSTRIAL MAINTENANCE</span>
  </div>

  <div class="contact-person">
    <p class="contact-person__name">Dale Virnow Jr.</p>
    <p class="contact-person__role">CEO &amp; Founder</p>
    <div class="contact-person__rule"></div>
  </div>

  <ul class="contact-list">
    <li class="contact-list__item">
      <svg class="contact-list__icon" viewBox="0 0 18 18" aria-hidden="true">
        <circle cx="9" cy="9" r="9" fill="#1c70bf"/>
        <path d="M6.2 4.5l1.6 2.2-1 1.1c.6 1.3 1.6 2.3 2.9 2.9l1.1-1 2.2 1.6-.8 1.6c-3.6-.3-6.6-3.3-6.9-6.9z" fill="#262626"/>
      </svg>
      <span>413-627-8154</span>
    </li>
    <li class="contact-list__item">
      <svg class="contact-list__icon" viewBox="0 0 18 18" aria-hidden="true">
        <circle cx="9" cy="9" r="9" fill="#1c70bf"/>
        <rect x="4.5" y="5.8" width="9" height="6.4" rx="0.8" fill="#262626"/>
        <path d="M4.8 6.2L9 9.4l4.2-3.2" fill="none" stroke="#1c70bf" stroke-width="1"/>
      </svg>
      <span>dale.virnow.jr@brindlemail.net</span>
    </li>
  </ul>
</section>

</body>
</html>
```